Bluebird Listings ad 2014 15

I need a design for an advertisement in our Bluebird Listings book telephone directory.
The directory runs for a 12 month period.

Our business offers 24 hour glass replacements to homes, shops and offices.
Our service is usually required by customers that require their glass replaced urgently
.
The ad is 1 of many in the directory offering the same service so we need to attract the customers attention quickly and easily and deliver our message - "24hr glass replacements to doors windows and shopfronts. Call now 9372 4816".

I want to keep the data in the attached ad but with a professional graphic presentation.

The ad size is 58mm high x 83mm wide, full colour.

Target Market(s)

Our customer is generally someone in need of an emergency repair. They aren't spending time shopping around for a product, they have a problem that they want fixed promptly and professionally.

Industry/Entity Type

Business

Font styles to use
Sans Serif

Colors
0255a3
f37022

Requirements
Must have
• "24HR" must stand out, this is a key aspect of our service. The ad needs to be clear and easy to read.

```html
<!DOCTYPE html>
<html lang="en">
<head>
<meta charset="utf-8">
<title>Steadfast Glass – 24 Hour Glass Replacement</title>
<link rel="stylesheet" href="https://fonts.googleapis.com/css2?family=Archivo+Black&family=Arimo:ital,wght@0,700;1,700&family=Oswald:wght@400&family=Roboto+Condensed:wght@400&family=Rubik+Dirt&family=Tinos&display=swap">
<style>
  :root {
    --brand-blue: #0255a3;
    --brand-orange: #f37022;
    --cream: #f3f1e6;
    --ink: #111111;
    --white: #ffffff;
    --steel: #a3a3a3;
    --glass-dark: #1f2a33;
    --glass-light: #8ea3b1;
    --italic-blue: #1a1ae6;
  }
  * { box-sizing: border-box; margin: 0; padding: 0; }
  html, body { width: 1200px; height: 839px; overflow: hidden; background: var(--cream); }
  .ad {
    position: relative; width: 1200px; height: 839px; overflow: hidden;
    background: var(--cream); font-family: "Archivo Black", sans-serif;
  }
  .hero {
    position: absolute; left: 0; top: 0; width: 1200px; height: 166px;
    background: radial-gradient(ellipse at 62% 40%, var(--glass-light) 0%, #4d5e6a 35%, var(--glass-dark) 80%);
  }
  .hero-title {
    position: absolute; left: 0; top: 14px; width: 1200px; text-align: center;
    font-family: "Rubik Dirt", sans-serif; font-weight: 400; font-size: 112px; line-height: 130px;
    color: var(--brand-orange); letter-spacing: 2px; white-space: nowrap;
  }
  .headline {
    position: absolute; left: 0; top: 178px; width: 1200px; text-align: center;
    font-size: 88px; line-height: 104px; color: var(--brand-blue); letter-spacing: 6px;
    white-space: nowrap;
  }
  .hours-badge {
    position: absolute; left: 37px; top: 285px; width: 242px; height: 229px;
    background: var(--brand-orange); padding: 9px;
  }
  .hours-badge-inner {
    width: 100%; height: 100%; border: 5px solid var(--white); background: var(--brand-blue);
    display: flex; flex-direction: column; align-items: center; justify-content: center;
  }
  .hours-number {
    font-family: "Arimo", sans-serif; font-style: normal; font-weight: 700;
    font-size: 150px; line-height: 130px; color: var(--white); letter-spacing: -8px;
  }
  .hours-word {
    font-family: "Tinos", serif; font-size: 44px; line-height: 44px; color: var(--white);
    margin-top: 2px;
  }
  .services { position: absolute; left: 310px; top: 291px; list-style: none; }
  .services li {
    display: flex; align-items: center; gap: 12px; height: 58px;
    font-family: "Oswald", sans-serif; font-size: 46px; letter-spacing: 5px; color: var(--ink);
    white-space: nowrap;
  }
  .services svg { width: 40px; height: 40px; flex: none; }
  .promise {
    position: absolute; left: 842px; top: 290px; width: 331px; height: 234px;
    background: var(--brand-orange); border-radius: 34px; text-align: center;
    font-family: "Arimo", sans-serif; font-style: italic; font-weight: 700;
    font-size: 37px; line-height: 58px; letter-spacing: 3px; padding-top: 2px;
    white-space: nowrap;
  }
  .promise .light { color: var(--white); }
  .promise .accent { color: var(--italic-blue); letter-spacing: 2px; }
  .tagline-band {
    position: absolute; left: 0; top: 539px; width: 1200px; height: 60px;
    background: var(--brand-orange); color: var(--white);
    font-family: "Roboto Condensed", sans-serif; font-size: 48px; line-height: 60px;
    letter-spacing: 0.4px; text-align: center; white-space: nowrap;
  }
  .call {
    position: absolute; left: 0; top: 600px; width: 1200px; text-align: center;
    font-size: 98px; line-height: 100px; color: var(--brand-orange); letter-spacing: 16px;
    white-space: nowrap;
  }
  .footer {
    position: absolute; left: 0; top: 702px; width: 1200px; height: 137px;
    background: linear-gradient(90deg, var(--brand-blue) 0 52%, var(--steel) 52% 100%);
  }
  .brand-name {
    position: absolute; left: 0; top: 6px; width: 1200px; text-align: center;
    font-family: "Arimo", sans-serif; font-style: normal; font-weight: 700;
    font-size: 76px; line-height: 86px; color: var(--white); letter-spacing: 1px;
  }
  .insurance {
    position: absolute; left: 0; top: 92px; width: 1200px; text-align: center;
    font-family: "Arimo", sans-serif; font-style: italic; font-weight: 700;
    font-size: 33px; line-height: 40px; color: var(--ink); letter-spacing: 6px;
  }
</style>
</head>
<body>
<div class="ad">
  <div class="hero" role="img" aria-label="Photograph of shattered window glass with radiating cracks"></div>
  <h1 class="hero-title">BROKEN GLASS?</h1>

  <h2 class="headline">WE CAN REPLACE IT</h2>

  <div class="hours-badge">
    <div class="hours-badge-inner">
      <span class="hours-number">24</span>
      <span class="hours-word">HOURS</span>
    </div>
  </div>

  <ul class="services">
    <li><svg viewBox="0 0 24 24"><polygon fill="#f37022" points="12,1 14.9,8.6 23,8.9 16.6,13.9 18.9,21.8 12,17.2 5.1,21.8 7.4,13.9 1,8.9 9.1,8.6"/></svg>DOOR GLASS</li>
    <li><svg viewBox="0 0 24 24"><polygon fill="#f37022" points="12,1 14.9,8.6 23,8.9 16.6,13.9 18.9,21.8 12,17.2 5.1,21.8 7.4,13.9 1,8.9 9.1,8.6"/></svg>WINDOW GLASS</li>
    <li><svg viewBox="0 0 24 24"><polygon fill="#f37022" points="12,1 14.9,8.6 23,8.9 16.6,13.9 18.9,21.8 12,17.2 5.1,21.8 7.4,13.9 1,8.9 9.1,8.6"/></svg>SHOWER GLASS</li>
    <li><svg viewBox="0 0 24 24"><polygon fill="#f37022" points="12,1 14.9,8.6 23,8.9 16.6,13.9 18.9,21.8 12,17.2 5.1,21.8 7.4,13.9 1,8.9 9.1,8.6"/></svg>SHOPFRONT GLASS</li>
  </ul>

  <div class="promise">
    <div class="light">QUALIFIED</div>
    <div class="light">TRADESMAN</div>
    <div class="accent">ALL WORK</div>
    <div class="accent">GUARANTEED</div>
  </div>

  <div class="tagline-band">To Regain SAFETY &amp; SECURITY In Your Home, SHop &amp; Office</div>

  <div class="call">CALL 9372 4816</div>

  <div class="footer">
    <div class="brand-name">Steadfast Glass</div>
    <div class="insurance">INSURANCE BILLED DIRECT</div>
  </div>
</div>
</body>
</html>
```